Estate Planner needs an Ad for a local newsletter

I need an ad designed for my practice as an estate planning attorney. The ad will be in a newsletter that targets individuals over the age of 55. My ad is 7.5"W x 4.6"H (a half page ad) .
The wording should include:
(No subject)
Whitcombe, Dana

Dana Whitcombe

Wisdom Meets Planning
Your Estate, Your Legacy

After 23 years as a military spouse, moving our family of six across the country,
I learned the true value of careful planning. Today I help Brevard County's seniors protect what matters most – their family’s future and their life’s work.

I understand that your estate is more than just assets – it's a lifetime of wise
decisions, cherished memories, and dreams for your family's future.

Professional Estate Planning:
• Wills & Living Trusts • Healthcare Directives
• Power of Attorney • Asset Protection
• Probate Avoidance • Peace of Mind

Plus also needs to have my contact information:
PRV Law
Dana Whitcombe
Attorney/Of Counsel
4630 Oakhollow Road
Melbourne, Florida 32901
(555) 814-0962
dwhitcombe@prvlawgroup.example
Logo is attached.

```html
<!DOCTYPE html>
<html lang="en">
<head>
<meta charset="utf-8">
<title>PRV Law – Estate Planning Ad</title>
<link rel="stylesheet" href="https://fonts.googleapis.com/css2?family=Barlow+Condensed:wght@500;600;700&family=Roboto+Condensed:wght@400&display=swap">
<style>
  :root {
    --teal-deep: #093a40;
    --teal: #0f4d53;
    --teal-light: #15585d;
    --white: #ffffff;
    --ink: #262b3d;
    --rule: #9fb8ba;
    --bronze: #6e5a44;
    --bronze-dark: #2c2a24;
  }
  * { margin: 0; padding: 0; box-sizing: border-box; }
  html, body { width: 1200px; height: 736px; overflow: hidden; }
  body { background: var(--teal-deep); }
  .ad {
    position: relative;
    width: 1200px;
    height: 736px;
    overflow: hidden;
    background: linear-gradient(100deg, var(--teal) 0%, var(--teal-light) 55%, var(--teal-deep) 100%);
    color: var(--white);
  }
  .justice-art {
    position: absolute;
    left: 700px;
    top: 150px;
    width: 500px;
    height: 586px;
    background:
      radial-gradient(ellipse 30% 48% at 78% 52%, rgba(150,120,85,0.75), rgba(110,90,68,0.35) 55%, transparent 75%),
      radial-gradient(ellipse 26% 16% at 30% 86%, rgba(44,42,36,0.9), rgba(44,42,36,0.4) 60%, transparent 80%),
      radial-gradient(ellipse 55% 12% at 62% 94%, rgba(110,90,68,0.55), transparent 80%);
  }
  .top-rule {
    position: absolute;
    top: 128px;
    height: 1px;
    background: var(--rule);
    opacity: 0.7;
  }
  .top-rule--left { left: 688px; width: 104px; }
  .top-rule--right { left: 1168px; width: 32px; }
  .firm-mark {
    position: absolute;
    left: 792px;
    top: 0;
    width: 376px;
    height: 146px;
    background: var(--white);
    display: flex;
    align-items: center;
    justify-content: center;
    gap: 14px;
  }
  .firm-mark__square { width: 18px; height: 18px; background: var(--ink); }
  .firm-mark__name {
    font-family: "Barlow Condensed", sans-serif;
    font-weight: 700;
    font-size: 64px;
    color: var(--ink);
    letter-spacing: 1px;
  }
  .headline {
    position: absolute;
    left: 46px;
    top: 26px;
    font-family: "Barlow Condensed", sans-serif;
    font-weight: 700;
    font-size: 72px;
    line-height: 72px;
    letter-spacing: 0.5px;
  }
  .story {
    position: absolute;
    left: 47px;
    top: 180px;
    font-family: "Roboto Condensed", sans-serif;
    font-weight: 400;
    font-size: 24.5px;
    line-height: 32.5px;
    letter-spacing: -0.4px;
    white-space: nowrap;
  }
  .services {
    position: absolute;
    left: 46px;
    top: 360px;
    font-family: "Barlow Condensed", sans-serif;
    font-weight: 600;
  }
  .services__title { font-size: 48px; line-height: 54px; }
  .services__list { list-style: none; font-size: 54px; line-height: 51px; white-space: nowrap; }
  .contact {
    position: absolute;
    left: 47px;
    top: 590px;
    font-family: "Barlow Condensed", sans-serif;
    font-weight: 600;
    font-size: 37px;
    line-height: 39px;
    letter-spacing: -1.2px;
  }
  .contact__role { font-weight: 500; font-size: 30px; margin-left: 8px; }
</style>
</head>
<body>
  <div class="ad">
    <div class="justice-art" role="img" aria-label="Bronze statue of Lady Justice holding scales and a sword, beside a wooden gavel on its block"></div>

    <div class="top-rule top-rule--left"></div>
    <div class="top-rule top-rule--right"></div>

    <div class="firm-mark">
      <span class="firm-mark__square"></span>
      <span class="firm-mark__name">PRV Law</span>
    </div>

    <h1 class="headline">Wisdom Meets Planning<br>Your Estate, Your Legacy</h1>

    <p class="story">
      After 23 years as a military spouse, moving our family of six across the country,<br>
      I learned the true value of careful planning. Today I help Brevard County's<br>
      seniors protect what matters most – their family’s future and their life’s work.<br>
      I understand that your estate is more than just assets – it's a lifetime of wise<br>
      decisions, cherished memories, and dreams for your family's future.
    </p>

    <section class="services">
      <h2 class="services__title">Professional Estate Planning:</h2>
      <ul class="services__list">
        <li>• Wills &amp; Living Trusts • Healthcare Directives</li>
        <li>• Power of Attorney • Asset Protection</li>
        <li>• Probate Avoidance • Peace of Mind</li>
      </ul>
    </section>

    <address class="contact" style="font-style: normal;">
      <div>Dana Whitcombe<span class="contact__role">Attorney/Of Counsel</span></div>
      <div>4630 Oakhollow Road, Melbourne, Florida 32901</div>
      <div>(555) 814-0962 . dwhitcombe@prvlawgroup.example</div>
    </address>
  </div>
</body>
</html>
```